Marta Business Card

My wife is going to start her own business with renting holiday appartments to tourists. She needs a design for a new business card... and a new web site.
Look at Stayvolt "Erholung auf dem Lindenwäldchen"

Target Market(s)

Give business card to prospects at any situation

Contact Information for Business Card

not sure what this means

Font styles to use
Script

Colors
fec41a
fee18a

Requirements
Must have
• My wife's handwriting is difficult to read:
Entspannen - Loslassen - Auftanken
Marta & das Lindenwäldchen
Urlaub an einem besonderen Ort
Marta Brecke
Grauer Pfad 7
18471 Alt Feldow
post@marta-brecke.de
www.lindenwaeldchen.net
Nice to have
• Beige background
Font like handwriting

```html
<!DOCTYPE html>
<html lang="de">
<head>
<meta charset="utf-8">
<title>Marta &amp; das Lindenwäldchen – Visitenkarte</title>
<link rel="stylesheet" href="https://fonts.googleapis.com/css2?family=Great+Vibes&family=Norican&display=swap">
<style>
  :root {
    --page-bg: #b3a779;
    --card-bg: #fee18a;
    --ink: #111008;
    --rule: #000000;
  }
  * { margin: 0; padding: 0; box-sizing: border-box; }
  html, body {
    width: 1174px;
    height: 1200px;
    overflow: hidden;
    background: var(--page-bg);
  }
  .business-card {
    position: absolute;
    left: 387px;
    top: 273px;
    width: 401px;
    height: 654px;
    background: var(--card-bg);
    color: var(--ink);
    font-family: "Great Vibes", cursive;
    text-align: center;
  }
  .rule {
    position: absolute;
    background: var(--rule);
  }
  .rule--wide {
    left: 26px;
    width: 349px;
    height: 4px;
  }
  .rule--short {
    left: 165px;
    width: 71px;
    height: 1px;
  }
  .line {
    position: absolute;
    left: 0;
    width: 100%;
    line-height: 1;
    white-space: nowrap;
  }
  .motto { font-size: 38px; }
  .business-name { font-size: 33px; }
  .business-claim { font-size: 27px; }
  .owner-name {
    font-family: "Norican", cursive;
    font-size: 23px;
  }
  .address { font-size: 27px; }
  .contact { font-size: 27px; }
</style>
</head>
<body>
  <main class="business-card">
    <div class="rule rule--wide" style="top:69px"></div>

    <p class="line motto" style="top:97px">Entspannen - Loslassen</p>
    <p class="line motto" style="top:144px">Auftanken</p>

    <div class="rule rule--wide" style="top:202px"></div>

    <p class="line business-name" style="top:291px">Marta &amp; das Lindenwäldchen</p>
    <p class="line business-claim" style="top:329px">Urlaub an einem besonderen Ort</p>

    <div class="rule rule--short" style="top:376px"></div>

    <p class="line owner-name" style="top:400px">Marta Brecke</p>
    <p class="line address" style="top:432px">Grauer Pfad 7</p>
    <p class="line address" style="top:465px">18471 Alt Feldow</p>

    <div class="rule rule--short" style="top:514px"></div>

    <p class="line contact" style="top:535px">post@marta-brecke.de</p>
    <p class="line contact" style="top:568px">www.lindenwaeldchen.net</p>
  </main>
</body>
</html>
```